CRESTLINE Academy Exhibit Booth Posters

My company is CRESTLINE Academy (a division of CRESTLINE for Growth). We are exhibiting in a month, and I need to re-do my exhibit booth posters. There will be a total of 4 posters needed. Sizes are below.
1) Top- 11 feet long X 12 inches wide (Try to match color scheme in example photo)
2) Center- 4 feet long X 2 feet wide (Chalkboard background)
3) Left- 18 inches long X 2 feet wide (Cork-board back ground with the use of push pins holding up post-it-notes, paper, etc.)
4) Right- 18 inches long X 2 feet wide (Cork-board back ground with the use of push pins holding up post-it-notes, paper, etc.)
I have attached a photo of my old booth. This will get you an idea of the size, color schemes, and more. I have created basic rendering of each poster. The content is important, but the look and design should be drastically improved.
The websites to look into for ideas are:
www.crestlineforgrowth.example
www.crestlineacademy.example
Updates
I've added a new file. It's a .JPG of the certification diploma. Thanks!
Target Market(s)
Business Owners, Managers, HR, Supervisors, Teens who want to boost their resume
Industry/Entity Type
It Company
Look and feel

```html
<!DOCTYPE html>
<html lang="en">
<head>
<meta charset="utf-8">
<title>CRESTLINE Academy – Booth Top Banner</title>
<link rel="stylesheet" href="https://fonts.googleapis.com/css2?family=Almendra:wght@400;700&display=swap">
<style>
  :root {
    --frame-dark: #6e2414;
    --frame-mid: #9c4a2c;
    --frame-light: #c07a55;
    --board-light: #6b7582;
    --board-mid: #58616d;
    --board-dark: #454c57;
    --headline-red: #e0121a;
    --headline-outline: #ffffff;
    --brand-blue: #2f6fd6;
    --brand-dot: #e8eef8;
  }
  html, body {
    margin: 0;
    padding: 0;
    width: 1200px;
    height: 144px;
    overflow: hidden;
    background: #ffffff;
  }
  .banner {
    position: relative;
    width: 1200px;
    height: 144px;
    box-sizing: border-box;
    border: 8px solid var(--frame-mid);
    border-top-color: var(--frame-light);
    border-left-color: var(--frame-light);
    border-bottom-color: var(--frame-dark);
    border-right-color: var(--frame-dark);
    box-shadow: inset 0 0 0 2px var(--frame-dark);
  }
  .board {
    position: absolute;
    inset: 2px;
    background:
      radial-gradient(ellipse at 30% 40%, var(--board-light) 0%, transparent 60%),
      radial-gradient(ellipse at 80% 70%, var(--board-light) 0%, transparent 55%),
      linear-gradient(180deg, var(--board-mid), var(--board-dark));
    box-shadow: inset 0 0 14px rgba(0,0,0,0.45);
  }
  .brand {
    position: absolute;
    left: 22px;
    top: 22px;
    width: 100px;
    height: 90px;
    display: flex;
    flex-direction: column;
    align-items: center;
    justify-content: center;
    gap: 4px;
  }
  .brand-dot {
    width: 26px;
    height: 26px;
    border-radius: 50%;
    background: var(--brand-dot);
  }
  .brand-name {
    margin: 0;
    font-family: "Almendra", serif;
    font-weight: 700;
    font-size: 15px;
    line-height: 1.05;
    text-align: center;
    color: var(--brand-blue);
  }
  .headline {
    position: absolute;
    left: 128px;
    top: 14px;
    width: 1050px;
    height: 100px;
  }
  .headline-text {
    font-family: "Almendra", serif;
    font-weight: 400;
    font-size: 62px;
    fill: var(--headline-red);
    stroke: var(--headline-outline);
    stroke-width: 5px;
    stroke-linejoin: round;
    paint-order: stroke fill;
  }
</style>
</head>
<body>
  <header class="banner">
    <div class="board">
      <div class="brand">
        <span class="brand-dot" aria-hidden="true"></span>
        <p class="brand-name">CRESTLINE<br>Academy</p>
      </div>
      <svg class="headline" viewBox="0 0 1050 100" aria-labelledby="headline-title">
        <title id="headline-title">The Solutions You’ve Been Looking For!</title>
        <text class="headline-text" x="6" y="72" textLength="1036" lengthAdjust="spacingAndGlyphs">The Solutions You’ve Been Looking For!</text>
      </svg>
    </div>
  </header>
</body>
</html>
```